Homepage Website Design for luxury picnic company

We need a homepage designed for a luxury picnic business to match our updated branding/logo which we're currently completing on ArtGatherly with another competition. Please see attached logo/colour example to use for now.

PLEASE NOTE: We are only after graphic design concepts as part of this competition. I will get another developer to actually code the website.

It is important that this website is very elegant/luxurious and stands out from a visual perspective. The images really need to match the content/sections also. The new branding colours are silver with a dark background. Please create the new website homepage to match these colours/branding.

Please create as many concepts as possible and then I will provide feedback from there

The website content including sections is here https://pages.velmoranote.com/doc/d/7kRtWq2mLp9XcVb4Hn8Js3Yd6Fg1Za5Qe0Uo2Ti/edit?mode=share

Images to use are located here https://vault.trenquilbox.com/vault/dirs/5HmQzR2-NcWy8Kp41-7VbLdTsXoeFj?mode=share and there is also lots of videos at this link which you can screenshot images out of if needed https://www.stashquarry.com/sh/k827trwm3hdz4/AACvnRt2Lm8WqPe5Xu9JdsYk?dl=0

Any questions please contact me

```html
<!DOCTYPE html>
<html lang="en">
<head>
<meta charset="utf-8">
<title>Ridgeline Picnics — Luxury picnics at breathtaking locations</title>
<link href="https://fonts.googleapis.com/css2?family=Lobster+Two:ital,wght@1,400;1,700&family=Lato:wght@300;400;700&display=swap" rel="stylesheet">
<style>
:root{
  --navy:#151a2b;
  --navy-2:#1d2336;
  --silver:#c3c3c3;
  --silver-light:#f1f1f1;
  --ink:#2b2b2b;
  --muted:#6e6e6e;
  --white:#ffffff;
  --accent:#e8c61a;
  --star:#f4b400;
  --link:#b3262e;
}
*{box-sizing:border-box;margin:0;padding:0}
html,body{width:1200px;height:5102px;overflow:hidden}
body{position:relative;background:var(--white);font-family:"Lato",sans-serif;color:var(--ink)}
.abs{position:absolute}
.script{font-family:"Lobster Two",cursive;font-style:italic;font-weight:400}
.spaced-title{font-family:"Lobster Two",cursive;font-style:italic;font-weight:400;font-size:26px;letter-spacing:22px;text-align:center;color:var(--ink);width:1200px;left:0}
.photo{position:absolute;overflow:hidden}

/* nav */
.site-nav{top:0;left:0;width:1200px;height:60px;background:var(--navy)}
.brand{position:absolute;left:150px;top:17px;color:var(--white);font-family:"Lato",sans-serif;font-weight:400;font-size:16px;display:flex;align-items:center;gap:8px}
.brand-dot{width:12px;height:12px;border-radius:50%;background:var(--silver)}
.menu{position:absolute;right:150px;top:22px;display:flex;gap:23px;font-size:13px;color:var(--white)}
.menu .current{color:#8d93a3}
.menu .hover{color:var(--silver)}

/* hero */
.hero{top:60px;left:0;width:1200px;height:570px;background:linear-gradient(90deg,#ffffff 0%,#ffffff 28%,#eef0f2 40%,#a9b3be 55%,#6d7683 70%,#4f4a4a 85%,#7a6a63 100%)}
.hero-title{position:absolute;left:148px;top:192px;font-size:38px;color:#1b1b1b}
.hero-sub{position:absolute;left:150px;top:258px;font-size:20px;letter-spacing:2.5px;color:#222;font-weight:400}
.btn-dark{position:absolute;display:flex;align-items:center;justify-content:center;background:var(--navy);color:var(--white);border-radius:22px;font-size:14px;font-weight:700;letter-spacing:2px}
.hero .btn-dark{left:148px;top:330px;width:210px;height:44px}
.badge{position:absolute;left:1073px;top:443px;width:114px;height:114px;border-radius:50%;background:#1e88d6;border:6px solid var(--white)}

/* as seen on */
.press{top:630px;left:0;width:1200px;height:75px;background:var(--silver)}
.press-label{position:absolute;left:152px;top:29px;font-size:13px;color:var(--white)}
.press-list{position:absolute;left:300px;top:25px;width:760px;display:flex;justify-content:space-between;font-size:17px;color:var(--white);font-weight:700}

/* feature rows */
.feature-img{height:195px;width:590px}
.feature-img.left{left:0;border-radius:0 160px 160px 0/0 98px 98px 0}
.feature-img.right{left:612px;border-radius:160px 0 0 160px/98px 0 0 98px}
.feature-title{position:absolute;font-family:"Lobster Two",cursive;font-style:italic;font-weight:400;font-size:20px;letter-spacing:16px;color:#1b1b1b}
.feature-text{position:absolute;width:445px;font-size:12.5px;line-height:22px;color:#333}

/* video */
.video{top:1440px;left:0;width:1200px;height:465px;background:radial-gradient(ellipse at 60% 30%,#b4607a 0%,#6f3445 30%,#3c2a2c 60%,#2a2425 100%)}
.play{position:absolute;border-radius:50%;background:var(--white);display:flex;align-items:center;justify-content:center}
.video .play{left:541px;top:165px;width:118px;height:118px}
.video-caption{position:absolute;left:0;bottom:0;width:1200px;height:52px;background:rgba(60,60,60,.55);color:var(--white);font-size:17px;letter-spacing:2px;text-align:center;line-height:52px}

/* prices */
.prices{top:2030px;left:0;width:1200px;height:283px;background:var(--navy);overflow:hidden}
.half-circle{position:absolute;top:6px;width:270px;height:270px;border-radius:50%;background:var(--silver)}
.price-col{position:absolute;top:46px;width:300px;text-align:center;color:var(--white)}
.price-col h3{font-weight:400;font-size:22px;letter-spacing:2.5px}
.price-col p{margin-top:14px;font-size:22px;letter-spacing:2.5px}
.price-divider{position:absolute;top:40px;width:2px;height:70px;background:#4a5064}
.btn-outline{position:absolute;display:flex;align-items:center;justify-content:center;border:2px solid var(--white);border-radius:24px;color:var(--white);font-size:14px;font-weight:700;letter-spacing:2px}
.prices .btn-outline{left:472px;top:166px;width:256px;height:44px}
.deposit{position:absolute;left:150px;top:253px;font-size:13px;letter-spacing:1.2px;color:var(--white)}
.deposit span{color:var(--accent);font-weight:700}

/* how it works */
.how{top:2375px;left:0;width:1200px;height:745px;background:var(--silver-light)}
.how .photo{left:0;top:0;width:512px;height:745px;background:linear-gradient(180deg,#8fa0b5 0%,#6e7d8c 30%,#7b8a91 55%,#c9c9d0 75%,#5c2f3c 100%)}
.how-title{position:absolute;left:612px;top:40px;font-size:28px;letter-spacing:7px}
.steps{position:absolute;left:565px;top:110px;list-style:none}
.steps li{display:flex;align-items:flex-start;height:77px}
.step-num{font-family:"Lobster Two",cursive;font-style:italic;font-size:44px;color:#8a8a8a;width:46px;line-height:44px}
.step-text{width:440px;font-size:15.5px;letter-spacing:1.3px;line-height:25px;color:#333}
.how .btn-dark{left:611px;top:650px;width:210px;height:42px}

/* spots */
.spots-intro{position:absolute;left:155px;top:3240px;width:890px;font-size:11.5px;line-height:27px;color:#444;text-align:left}
.spots{top:3357px;left:0;width:1200px;height:400px;background:var(--navy)}
.spot-card{position:absolute;top:45px;width:428px;height:285px;background:linear-gradient(180deg,#8a9bb2 0%,#5d6d80 40%,#8a7c80 70%,#4b3b44 100%)}
.spot-card .play{left:178px;top:105px;width:74px;height:74px}
.spot-bar{position:absolute;left:0;bottom:0;width:100%;height:30px;background:rgba(70,70,70,.55);color:var(--white);display:flex;justify-content:space-between;align-items:center;padding:0 6px}
.spot-bar .name{font-size:17px;letter-spacing:1.5px}
.spot-bar .link{font-size:12.5px;font-weight:700;letter-spacing:1.2px}
.spots-note{position:absolute;left:150px;top:365px;width:900px;font-size:9px;letter-spacing:1.4px;line-height:12px;color:#d7d7d7}

/* food */
.food{top:3885px;left:0;width:1200px;height:555px;background:linear-gradient(100deg,#1d2a3a 0%,#26354a 40%,#2d3848 60%,#6e5f3b 80%,#3a3320 100%)}
.food-copy{position:absolute;left:150px;top:32px;width:535px;color:var(--white);font-size:12.5px;line-height:25px}
.food-copy p+p{margin-top:22px}
.food-list{margin-top:18px;list-style:none}
.food-list li{position:relative;padding-left:30px;line-height:26px}
.food-list li::before{content:"";position:absolute;left:0;top:10px;width:7px;height:7px;border-radius:50%;background:var(--white)}
.food .btn-outline{left:150px;top:478px;width:210px;height:44px}

/* testimonials */
.testi-card{position:absolute;top:4570px;width:283px;height:170px;background:#f4f4f4;border:1px solid #e8e8e8;padding:16px 18px}
.testi-head{display:flex;align-items:center;gap:12px}
.avatar{width:40px;height:40px;border-radius:50%;background:#c9c0b8}
.testi-name{font-size:12.5px;color:#555}
.stars{display:flex;gap:4px;margin-left:4px}
.testi-text{margin-top:16px;font-size:11.5px;line-height:18px;color:#9a9a9a}
.testi-text a{color:var(--link);text-decoration:none}
.testi-date{position:absolute;right:22px;bottom:16px;font-size:10.5px;color:#8a8a8a}
.arrow{position:absolute;top:4640px;width:28px;height:28px;border-radius:50%;display:flex;align-items:center;justify-content:center}

/* footer */
.site-footer{top:4795px;left:0;width:1200px;height:307px;background:var(--navy);color:var(--white)}
.f-col{position:absolute;top:37px}
.f-col h4{font-size:15px;font-weight:700;letter-spacing:.5px;margin-bottom:24px}
.f-col ul{list-style:none;font-size:12.5px;line-height:33px}
.f-col p{font-size:12.5px;line-height:27px}
.form-grid{display:grid;grid-template-columns:140px 140px;gap:8px 8px}
.field{height:28px;border:1px solid #d9d9d9;background:var(--white);color:#9a9a9a;font-size:9px;padding:8px 6px}
.field.wide{grid-column:1/3;height:58px}
.send{margin-top:12px;width:140px;height:28px;border:1px solid var(--white);border-radius:4px;text-align:center;line-height:26px;font-size:12px}
.copyright{position:absolute;left:0;top:283px;width:1200px;text-align:center;font-size:9px;color:#c9c9c9}
</style>
</head>
<body>

<header class="abs site-nav">
  <div class="brand"><span class="brand-dot"></span>Ridgeline Picnics</div>
  <nav class="menu">
    <span class="current">Home</span><span class="hover">Pricing</span><span>Picnic Spots</span><span>Food</span><span>About Us</span><span>Testimonials</span><span>FAQ</span><span>Contact Us</span>
  </nav>
</header>

<section class="abs hero" role="img" aria-label="Woman in a hat pouring sparkling wine at a picnic on a mountain cliff edge at sunset">
  <h1 class="hero-title script">Share an unforgettable moment</h1>
  <p class="hero-sub">Luxury picnics at breathtaking locations</p>
  <div class="btn-dark">Book your picnic</div>
  <div class="badge" aria-label="Safety certification badge"></div>
</section>

<section class="abs press">
  <span class="press-label">As seen on:</span>
  <div class="press-list"><span>Skylantern</span><span>Norvale</span><span>Quilby</span><span>Tessen</span><span>Orbitra</span><span>Pellwood</span><span>Tessen</span></div>
</section>

<div class="photo feature-img left" style="top:765px;background:linear-gradient(90deg,#5d6f84 0%,#8a8f95 35%,#3f3a36 65%,#8d7b74 100%)" role="img" aria-label="Couple toasting with champagne at a cliff-top picnic"></div>
<h2 class="feature-title" style="left:612px;top:806px">BLISS</h2>
<p class="feature-text" style="left:612px;top:850px">We enable you to enjoy true quality time with your partner, friends or family. We do this by creating the perfect atmosphere to celebrate a special moment in your life or to simply spoil yourself!</p>

<h2 class="feature-title" style="left:150px;top:1016px">UNWIND</h2>
<p class="feature-text" style="left:150px;top:1060px">Let us do everything for you so you can enjoy a stress free experience. You will also discover the Blue Mountains like you never have before! Each of our picnic spots are absolutely stunning and also very private.</p>
<div class="photo feature-img right" style="top:975px;background:linear-gradient(180deg,#b6c3d3 0%,#8394aa 45%,#3f4b56 70%,#2b3138 100%)" role="img" aria-label="Blue mountain valley and cliffs under a soft sky"></div>

<div class="photo feature-img left" style="top:1185px;background:linear-gradient(90deg,#4f5d6c 0%,#9aa4ae 30%,#d7d8da 55%,#7f868d 80%,#3d3a3a 100%)" role="img" aria-label="Bottles of wine on ice and glassware on a picnic table"></div>
<h2 class="feature-title" style="left:612px;top:1227px">INDULGE</h2>
<p class="feature-text" style="left:612px;top:1271px">Our delicious picnics will have your mouth watering! You can design your own picnic by choosing from our extensive menu along with 2 choices of your favourite beverages. We cater for all dietary requirements.</p>

<section class="abs video" role="img" aria-label="Close-up of pink flowers and an engagement ring box on a picnic rug">
  <div class="play"><svg width="48" height="54" viewBox="0 0 48 54"><path d="M6 2 L46 27 L6 52 Z" fill="#111"/></svg></div>
  <div class="video-caption">Discover exactly how our picnic work in only 90 seconds</div>
</section>

<h2 class="abs spaced-title" style="top:1962px">OUR PRICES</h2>
<section class="abs prices">
  <div class="half-circle" style="left:-160px"></div>
  <div class="half-circle" style="left:1090px"></div>
  <div class="price-col" style="left:113px"><h3>GOURMET PICNIC</h3><p>$350 + GST</p></div>
  <div class="price-divider" style="left:449px"></div>
  <div class="price-col" style="left:447px"><h3>BYO PICNIC</h3><p>$200 + GST</p></div>
  <div class="price-divider" style="left:744px"></div>
  <div class="price-col" style="left:785px"><h3>PROPOSAL PICNIC</h3><p>$100 + GST</p></div>
  <div class="btn-outline">View package details</div>
  <p class="deposit">To secure your booking, all we need is a $100 + GST deposit. We offer custom payment plans at no extra cost. <span>Learn More</span></p>
</section>

<section class="abs how">
  <div class="photo" role="img" aria-label="Picnic cushions and glasses set up on a cliff overlooking the valley"></div>
  <h2 class="how-title script">HOW OUR PICNICS WORK</h2>
  <ol class="steps">
    <li><span class="step-num">1</span><span class="step-text">You can see packages, locations, available dates and times via our website.</span></li>
    <li><span class="step-num">2</span><span class="step-text">Select and book your type of picnic and location including date and time.</span></li>
    <li><span class="step-num">3</span><span class="step-text">You can also select your food, beverages and chalkboard message quickly and easily.</span></li>
    <li><span class="step-num">4</span><span class="step-text">We email you all the important information in the lead up to your picnic.</span></li>
    <li><span class="step-num">5</span><span class="step-text">Discover your stunning picnic spot where your picnic setting will be set up.</span></li>
    <li><span class="step-num">6</span><span class="step-text">We provide your choice of still or sparkling water chilled on ice for every picnic</span></li>
    <li><span class="step-num">7</span><span class="step-text">We will also deliver your food and drinks if you choose the catered option.</span></li>
  </ol>
  <div class="btn-dark">Book your picnic</div>
</section>

<h2 class="abs spaced-title" style="top:3178px">OUR PICNIC SPOTS</h2>
<p class="spots-intro">You will love our breathtaking locations which you can't find on Searchly! The only way to experience these stunning spots first hand is by organising a picnic with us. We have handpicked the absolute best picnic spots in the Blue Mountains from years of local knowledge. They're all accessible with regular vehicles and only a short walk from where you park. Our spots are very quiet giving you a peaceful and unique glimpse of the Blue Mountains.</p>

<section class="abs spots">
  <div class="spot-card" style="left:152px" role="img" aria-label="Picnic setup on a rocky lookout at Wentworth Falls">
    <div class="play"><svg width="28" height="32" viewBox="0 0 28 32"><path d="M3 1 L27 16 L3 31 Z" fill="#111"/></svg></div>
    <div class="spot-bar"><span class="name">Wentworth Falls</span><span class="link">View available dates and times</span></div>
  </div>
  <div class="spot-card" style="left:623px" role="img" aria-label="Picnic setup with lanterns on a cliff at Katoomba">
    <div class="play"><svg width="28" height="32" viewBox="0 0 28 32"><path d="M3 1 L27 16 L3 31 Z" fill="#111"/></svg></div>
    <div class="spot-bar"><span class="name">Katoomba</span><span class="link">View available dates and times</span></div>
  </div>
  <p class="spots-note">IMPORTANT NOTE: We don't publicly advertise our exact locations so we can continue to keep them a secret. For this reason we provide our clients with the directions the day prior to the picnic and ask that you do not share the exact location!</p>
</section>

<h2 class="abs spaced-title" style="top:3812px">FOOD &amp; BEVERAGES</h2>
<section class="abs food" role="img" aria-label="Wine glass and cheese on a picnic table at dusk">
  <div class="food-copy">
    <p>Our delicious food and beverages will have your mouth watering regardless of your tastes or dietary requirements. Our Gourmet Picnic menu is fully customisable so you can design your own picnic. We cater for allergies, vegans, celiacs and all other dietary requirements.</p>
    <p>We focus on offering diversity with the finest ingredients. We are a registered food business meaning we prepare, store and transport our food in accordance with all food handling guidelines. We have also put a lot of thought into the logistics of serving this food at our picnic locations and ensure the food is as refrigerated and fresh as possible. Each Gourmet Picnic includes the following:</p>
    <ul class="food-list">
      <li>2 choices of cheese, dips or antipasto</li>
      <li>2 choices of crackers</li>
      <li>Seasonal fruit</li>
      <li>1 choice of nuts or dried fruit</li>
      <li>1 choice of chocolate</li>
      <li>2 choices of complimentary beer, wine or non-alcoholic beverages</li>
    </ul>
  </div>
  <div class="btn-outline">Book your picnic</div>
</section>

<h2 class="abs spaced-title" style="top:4495px">TESTIMONIALS</h2>

<div class="arrow" style="left:33px;border:1px solid #bbb;background:#d6d6d6"><svg width="12" height="12" viewBox="0 0 12 12"><path d="M8 1 L3 6 L8 11" stroke="#fff" stroke-width="2" fill="none"/></svg></div>
<div class="arrow" style="left:1139px;background:#111"><svg width="12" height="12" viewBox="0 0 12 12"><path d="M4 1 L9 6 L4 11" stroke="#fff" stroke-width="2" fill="none"/></svg></div>

<article class="testi-card" style="left:150px">
  <div class="testi-head"><span class="avatar" role="img" aria-label="Customer portrait"></span><span class="testi-name">Dylan Harrow</span>
    <span class="stars"><svg width="84" height="14" viewBox="0 0 84 14"><g fill="#f4b400"><path id="s" d="M7 0 L9 5 L14 5 L10 8 L11.5 13.5 L7 10.3 L2.5 13.5 L4 8 L0 5 L5 5 Z"/><use href="#s" x="17"/><use href="#s" x="34"/><use href="#s" x="51"/><use href="#s" x="68"/></g></svg></span></div>
  <p class="testi-text">Best picnic I have ever had. Everything was organised to the smallest detail. My girlfriend and I had a lovely... <a>Read More</a></p>
  <span class="testi-date">2 days ago</span>
</article>
<article class="testi-card" style="left:458px">
  <div class="testi-head"><span class="avatar" role="img" aria-label="Customer portrait"></span><span class="testi-name">Dylan Harrow</span>
    <span class="stars"><svg width="84" height="14" viewBox="0 0 84 14"><g fill="#f4b400"><use href="#s"/><use href="#s" x="17"/><use href="#s" x="34"/><use href="#s" x="51"/><use href="#s" x="68"/></g></svg></span></div>
  <p class="testi-text">Best picnic I have ever had. Everything was organised to the smallest detail. My girlfriend and I had a lovely... <a>Read More</a></p>
  <span class="testi-date">2 days ago</span>
</article>
<article class="testi-card" style="left:766px">
  <div class="testi-head"><span class="avatar" role="img" aria-label="Customer portrait"></span><span class="testi-name">Dylan Harrow</span>
    <span class="stars"><svg width="84" height="14" viewBox="0 0 84 14"><g fill="#f4b400"><use href="#s"/><use href="#s" x="17"/><use href="#s" x="34"/><use href="#s" x="51"/><use href="#s" x="68"/></g></svg></span></div>
  <p class="testi-text">Best picnic I have ever had. Everything was organised to the smallest detail. My girlfriend and I had a lovely... <a>Read More</a></p>
  <span class="testi-date">2 days ago</span>
</article>

<footer class="abs site-footer">
  <div class="f-col" style="left:150px"><h4>Quick Navigation</h4><ul><li>Home</li><li>Pricing</li><li>Picnic Spots</li><li>Food</li><li>About Us</li></ul></div>
  <div class="f-col" style="left:322px"><h4>Company Information</h4><ul><li>Common Questions (FAQ)</li><li>Privacy Policy</li><li>Terms &amp; Conditions</li></ul></div>
  <div class="f-col" style="left:528px"><h4>Contact Details</h4><p>PO Box 1180 FERNVALE<br>NSW 2790, 02 5550 1427<br>hello@ridgelinepicnics.com.au</p></div>
  <div class="f-col" style="left:752px"><h4>Send Us a Message</h4>
    <div class="form-grid">
      <div class="field">First Name</div><div class="field">Last Name</div>
      <div class="field">Email Address</div><div class="field">Phone Number</div>
      <div class="field wide">Write Your Message</div>
    </div>
    <div class="send">Send</div>
  </div>
  <p class="copyright">Copyright © 2020 Ridgeline Picnics</p>
</footer>

</body>
</html>
```